Business Card Design with new logo

Warren Peltzman 4175
E 118th Rd Orlin, IL 62499
Cell: 217-555-0187
peltzmanrebuilds@mailhollow.com

Classic Car Restoration Services Buy Sell Trade Consign

Contact Information for Business Card

Warren Peltzman 9698
Cell: 217-555-0187

```html
<!DOCTYPE html>
<html lang="en">
<head>
<meta charset="utf-8">
<title>Larkmont Restoration LLC — Business Card</title>
<link href="https://fonts.googleapis.com/css2?family=Arimo:wght@400;700&display=swap" rel="stylesheet">
<style>
  :root {
    --backdrop: #e9e9ea;
    --card-white: #f5f4f4;
    --card-navy: #112231;
    --brand-red: #c9232b;
    --ink: #1b1f24;
    --rule: #b9b9bb;
    --white: #ffffff;
  }
  * { margin: 0; padding: 0; box-sizing: border-box; }
  html, body { width: 1000px; height: 1200px; overflow: hidden; }
  body {
    background: var(--backdrop);
    font-family: "Arimo", Arial, sans-serif;
    position: relative;
  }
  .card {
    position: absolute;
    left: 214px;
    width: 578px;
    height: 357px;
    box-shadow: 2px 3px 5px rgba(0,0,0,0.35);
  }
  .card-front {
    top: 218px;
    background: var(--card-white);
    border-radius: 0 62px 0 62px;
  }
  .card-back {
    top: 606px;
    background: var(--card-navy);
    border-radius: 62px 0 62px 0;
  }
  .brand {
    position: absolute;
    display: flex;
    flex-direction: column;
    align-items: center;
  }
  .brand-mark {
    border-radius: 50%;
    background: var(--brand-red);
  }
  .brand-name {
    font-weight: 700;
    color: var(--ink);
    text-transform: uppercase;
    text-align: center;
    line-height: 1.15;
  }
  .card-front .brand { left: 272px; top: 40px; width: 276px; }
  .card-front .brand-mark { width: 62px; height: 62px; margin-bottom: 16px; }
  .card-front .brand-name { font-size: 27px; letter-spacing: 1px; }
  .card-front .brand-name small { display: block; font-size: 14px; letter-spacing: 5px; }
  .card-back .brand { left: 100px; top: 92px; width: 378px; }
  .card-back .brand-mark { width: 82px; height: 82px; margin-bottom: 22px; }
  .card-back .brand-name { font-size: 37px; letter-spacing: 1px; color: var(--white); }
  .card-back .brand-name small { display: block; font-size: 17px; letter-spacing: 7px; margin-top: 6px; }

  .person { position: absolute; left: 30px; top: 194px; }
  .person-name { font-size: 20px; font-weight: 700; color: var(--ink); letter-spacing: 0.2px; }
  .person-name .first { color: var(--brand-red); }
  .person-role { font-size: 15px; color: var(--ink); margin-top: 2px; }
  .divider {
    position: absolute; left: 30px; top: 247px; width: 516px;
    height: 1px; background: var(--rule);
  }
  .contact {
    position: absolute; left: 30px; top: 261px;
    font-size: 15px; color: var(--ink); line-height: 20px; list-style: none;
  }
  .contact li { display: flex; align-items: center; gap: 5px; }
  .contact svg { width: 12px; height: 12px; fill: var(--brand-red); }
  .address {
    position: absolute; right: 32px; top: 261px;
    font-size: 15px; color: var(--ink); line-height: 20px;
    text-align: right; font-style: normal;
  }
</style>
</head>
<body>
  <section class="card card-front">
    <div class="brand">
      <span class="brand-mark"></span>
      <div class="brand-name">Larkmont<small>Restoration LLC</small></div>
    </div>
    <div class="person">
      <div class="person-name"><span class="first">DANIEL</span> FERRIS</div>
      <div class="person-role">Managing Director</div>
    </div>
    <div class="divider"></div>
    <ul class="contact">
      <li>
        <svg viewBox="0 0 12 12" aria-hidden="true"><path d="M1 3.5C1 2 2.5 1 6 1s5 1 5 2.5V5H8.5V3.8h-5V5H1z M3 5.5h6l1.5 5.5h-9z"/></svg>
        217-555-0187
      </li>
      <li>
        <svg viewBox="0 0 12 12" aria-hidden="true"><path d="M1 2.5h10v7H1z" /><path d="M1 2.5l5 4 5-4" fill="none" stroke="#f5f4f4" stroke-width="1.1"/></svg>
        peltzmanrebuilds@mailhollow.com
      </li>
    </ul>
    <address class="address">Warren Peltzman 4175<br>E 118th Rd Orlin, IL 62499</address>
  </section>

  <section class="card card-back">
    <div class="brand">
      <span class="brand-mark"></span>
      <div class="brand-name">Larkmont<small>Restoration LLC</small></div>
    </div>
  </section>
</body>
</html>
```